Choc biz start-up needs packaging design

We are a start-up chocolate company called 'Maison Verlaque Confections'. Our motto is 'Craft Beyond the Ordinary'. Themes associated with the company are: quality, social change, environmental awareness, innovation, refined and modern (with a strong emphasis on 'refined' - but not to the point of being boring!). Our product consists of bite-sized chocolate pieces. Being in the modern style, our products will utilise colour similar to www.tarvelbrookconfections.com, but with more restraint (that is, with a greater emphasis on the natural colours of chocolate: so the shades of white, milk and dark choc). We require a design for the exterior of both the LID and BASE.
More info:
---------------------------
Box shape and structure: See File 'cimg5416'
Logo: A logo has already been prepared, see 'AI-CMYK'. The main theme implied by this logo, is of 'nobility'. The style of lion itself is called a heraldic lion and traces back to European nobility. The colour of the logo is not fixed.
Product/Company info: See File 'back 3c', this text will need to go on the back of the box but how it appears is for you to decide
Dimensions (approx): note the length and width may vary but the height will stay at 33mm. This is because the design will be used for 9, 16 and 25 piece boxes.
Of entire box: 150mm x 150mm x 33mm high
Of lid: 150mm x 150mm x 23mm high (note this means that the base will be visible from the sides, when the box is closed)
Colours to avoid: large amounts of black and/or white
Colours to use: branding colours not yet determined so the designer is welcome to use any colours that s/he wishes.
File format: will require file to eventually be provided in vector format
Other: packaging will be CMYK printed and can be either matte/gloss laminated. To reduce costs, there will be no heat-stamping/embossing/etc.
Thoughts on other choc packaging:
File named '626808': Nice, but a little too plain and static (for what I'm after).
File named 'index3': Nice, but too traditional (for what I'm after).
File named 'imagesc': Nice, a little too modern and simple (for what I'm after). To me, it doesn't say refined enough.
File named '12cm cover colour a': This was the design that I'd been working on. But I'm not a graphic designer, it looks incomplete and I feel that it's incorporating elements potentially too ornate to incorporate into the overall company branding. I'm just as likely to choose an all-new design that I like than to pick one that improves upon what I'd started (assuming the issues I had with the design are also addressed).
Updates
For those who read the brief on the 6th of July, or earlier:
It's come to my attention that the file numbers referred to in the brief did not match the file numbers that I uploaded (PixelGuild somehow jumbled it all up). I've since edited the brief to make references to the file names and not numbers. My apologies for any confusion caused.
Industry/Entity Type
Chocolate Company
Look and feel
Each slider illustrates characteristics of the customer's brand and the style your logo design should communicate.

```html
<!DOCTYPE html>
<html lang="en">
<head>
<meta charset="utf-8">
<title>Maison Verlaque Confections – Lid</title>
<link rel="stylesheet" href="https://fonts.googleapis.com/css2?family=Cinzel:wght@400&display=swap">
<style>
  :root {
    --page: #ffffff;
    --lid: #d1cdbb;
    --lid-shadow: #a99d88;
    --lid-lip: #c2b8aa;
    --band: #838070;
    --band-top: #6f6a5a;
    --band-line: #f2ecd8;
    --stitch: #a3261b;
    --ribbon: #6e2606;
    --cream: #f6f0df;
    --mark-bg: #000000;
    --copy: #b3ae9d;
    --dots: #f1ecdd;
  }
  html, body {
    margin: 0;
    padding: 0;
    width: 1187px;
    height: 1200px;
    overflow: hidden;
    background: var(--page);
  }
  .canvas {
    position: relative;
    width: 1187px;
    height: 1200px;
    font-family: "Cinzel", serif;
  }
  .lid {
    position: absolute;
    left: 110px;
    top: 124px;
    width: 973px;
    height: 959px;
    background: var(--lid);
    box-shadow: inset 0 0 38px 10px var(--lid-shadow);
    border-bottom: 4px solid var(--lid-lip);
    overflow: hidden;
  }
  .stitch {
    position: absolute;
    top: 0;
    width: 3px;
    height: 501px;
    background: repeating-linear-gradient(to bottom, var(--stitch) 0 3px, transparent 3px 14px);
  }
  .stitch--left { left: 341px; }
  .stitch--right { left: 632px; }
  .band {
    position: absolute;
    left: 359px;
    top: 0;
    width: 254px;
    height: 499px;
    background: linear-gradient(to bottom, var(--band-top) 0, var(--band) 60px);
    border: 1.5px solid var(--band-line);
    border-top: none;
  }
  .brand-mark {
    position: absolute;
    left: 388px;
    top: 34px;
    width: 202px;
    height: 200px;
    background: var(--mark-bg);
    border: 1.5px solid var(--band-line);
    display: flex;
    flex-direction: column;
    align-items: center;
    justify-content: center;
    gap: 14px;
    box-sizing: border-box;
  }
  .brand-mark__square {
    width: 34px;
    height: 34px;
    background: var(--cream);
  }
  .brand-mark__name {
    margin: 0;
    color: var(--cream);
    font-size: 15px;
    letter-spacing: 1.5px;
    text-align: center;
    line-height: 1.35;
    text-transform: uppercase;
  }
  .ribbon {
    position: absolute;
    left: 200px;
    top: 379px;
    width: 582px;
    height: 60px;
    margin: 0;
    background: var(--ribbon);
    border: 1.5px solid var(--band-line);
    box-sizing: border-box;
    display: flex;
    align-items: center;
    justify-content: center;
    color: var(--cream);
    font-size: 15px;
    letter-spacing: 9px;
    text-transform: uppercase;
  }
  .dotted-rule {
    position: absolute;
    left: 55px;
    width: 890px;
    height: 3px;
    background: repeating-linear-gradient(to right, var(--dots) 0 3px, transparent 3px 12.5px);
  }
  .dotted-rule--top { top: 666px; }
  .dotted-rule--bottom { top: 850px; }
  .story {
    position: absolute;
    left: 48px;
    top: 686px;
    width: 903px;
    margin: 0;
    color: var(--copy);
    font-size: 27px;
    line-height: 36px;
    text-transform: uppercase;
    letter-spacing: 3px;
  }
  .story__line {
    display: block;
    white-space: nowrap;
    text-align: justify;
    text-align-last: justify;
  }
  .signature {
    position: absolute;
    left: 46px;
    top: 864px;
    width: 907px;
    height: 70px;
    margin: 0;
    display: flex;
    justify-content: space-between;
    align-items: center;
    color: var(--cream);
    font-size: 58px;
    line-height: 70px;
    font-weight: 400;
    text-transform: uppercase;
  }
  .signature__gap { width: 0; }
</style>
</head>
<body>
  <div class="canvas">
    <section class="lid" aria-label="Chocolate box lid">
      <div class="stitch stitch--left"></div>
      <div class="stitch stitch--right"></div>
      <div class="band"></div>
      <div class="brand-mark">
        <div class="brand-mark__square"></div>
        <p class="brand-mark__name">Maison Verlaque<br>Confections</p>
      </div>
      <p class="ribbon">Craft Beyond the Ordinary</p>

      <div class="dotted-rule dotted-rule--top"></div>
      <p class="story">
        <span class="story__line">These hand crafted bite sized morsels are</span>
        <span class="story__line">unique &amp; delectable made with the finest</span>
        <span class="story__line">selection of cocoa farmed ethically &amp;</span>
        <span class="story__line">sustainably delight in the experience that is</span>
      </p>
      <div class="dotted-rule dotted-rule--bottom"></div>
      <h1 class="signature" aria-label="Maison Verlaque">
        <span aria-hidden="true">M</span><span aria-hidden="true">A</span><span aria-hidden="true">I</span><span aria-hidden="true">S</span><span aria-hidden="true">O</span><span aria-hidden="true">N</span><span class="signature__gap" aria-hidden="true"></span><span aria-hidden="true">V</span><span aria-hidden="true">E</span><span aria-hidden="true">R</span><span aria-hidden="true">L</span><span aria-hidden="true">A</span><span aria-hidden="true">Q</span><span aria-hidden="true">U</span><span aria-hidden="true">E</span>
      </h1>
    </section>
  </div>
</body>
</html>
```